IT Consulting Business Card Design

We need a business card on our company name....which is a IT consulting and staffing company. We also train masters graduates in various IT courses. 70% of the time these cards will be handed out to the graduate students at the universities. 30% for our clients and business partners. We are uploading our company logo...would like to see something that matches our logo or blends with it. Please visit www.brightvaleworks.com for more details on logo and colors.

Target Market(s)

70% of the time these cards will be handed out to the graduate students at the universities. 30% for our clients and business partners.

Industry/Entity Type

Business

Contact Information for Business Card

Ravi Kondamuri
Vice-President
Bright Vale Works Inc
3807 Morrow Lane, Suite 412
East Brookridge, NJ 07315
ravi@brightvaleworks.com
Office : 1-866-219-3840 X 515
Cell number : 732-581-9034

Requirements
Nice to have
• may be company logo and name on the back of the card and detials on the other side...just a thought..!!

```html
<!DOCTYPE html>
<html lang="en">
<head>
<meta charset="utf-8">
<title>Bright Vale Works – Business Card</title>
<link rel="stylesheet" href="https://fonts.googleapis.com/css2?family=Alegreya+SC:ital,wght@0,400;1,400&family=Fira+Sans+Extra+Condensed:wght@700&display=swap">
<style>
  :root {
    --card-bg: #ffffff;
    --brand-red: #e51c1c;
    --ink: #141414;
    --slate: #7b8787;
    --mark-tint: #e51c1c;
  }
  html, body {
    margin: 0;
    padding: 0;
    width: 1200px;
    height: 702px;
    overflow: hidden;
    background: var(--card-bg);
  }
  .card {
    position: relative;
    width: 1200px;
    height: 702px;
    background: var(--card-bg);
  }
  .brand {
    position: absolute;
    left: 107px;
    top: 135px;
    width: 407px;
    text-align: center;
  }
  .brand-dot {
    display: block;
    width: 200px;
    height: 200px;
    margin: 0 auto 0 86px;
    border-radius: 50%;
    background: var(--mark-tint);
  }
  .brand-name {
    position: absolute;
    left: 0;
    top: 257px;
    width: 407px;
    margin: 0;
    font-family: "Fira Sans Extra Condensed", "Arial Narrow", sans-serif;
    font-weight: 700;
    font-size: 58px;
    line-height: 1;
    color: var(--brand-red);
    white-space: nowrap;
    text-align: left;
    letter-spacing: 0.2px;
  }
  .person {
    position: absolute;
    left: 650px;
    top: 150px;
  }
  .person-name {
    margin: 0;
    font-family: "Alegreya SC", Georgia, serif;
    font-style: italic;
    font-weight: 400;
    font-size: 54px;
    line-height: 1;
    color: var(--ink);
    white-space: nowrap;
  }
  .person-title {
    margin: 14px 0 0 7px;
    font-family: "Alegreya SC", Georgia, serif;
    font-size: 19px;
    line-height: 1;
    letter-spacing: 1px;
    color: var(--slate);
  }
  .contact {
    position: absolute;
    left: 653px;
    top: 400px;
    margin: 0;
    padding: 0;
    list-style: none;
    font-family: "Alegreya SC", Georgia, serif;
    font-style: italic;
    color: var(--slate);
  }
  .contact li {
    line-height: 1;
    white-space: nowrap;
  }
  .contact-phone { font-size: 38px; }
  .contact-email { font-size: 31px; margin-top: 24px; }
  .contact-web { font-size: 31px; margin-top: 30px; color: var(--brand-red); }
  .label { margin-right: 6px; }
</style>
</head>
<body>
  <main class="card">
    <section class="brand">
      <span class="brand-dot" aria-hidden="true"></span>
      <p class="brand-name">BRIGHT VALE WORKS</p>
    </section>

    <section class="person">
      <h1 class="person-name">Ravi Kondamuri</h1>
      <p class="person-title">VICE-PRESIDENT</p>
    </section>

    <ul class="contact">
      <li class="contact-phone"><span class="label">T :</span>732-581-9034</li>
      <li class="contact-email"><span class="label">E :</span>ravi@brightvaleworks.com</li>
      <li class="contact-web">www.brightvaleworks.com</li>
    </ul>
  </main>
</body>
</html>
```